Vorquel 820 practise with the goal to have business and people Lifted past the horizon

We need a logo design for business cards for a company based in Australia Called TALBrookWare. We specialise in cloud tech from th full Quenfield stack. i would like it to be close to quenfield colours and we specilise in Quenfield Vorquel 820 Client Outreach. the design should display the confidence an security of a cloud based company. the tag line of Lifted past the horizon in the company motto.

Target Market(s)

I am targeting small to medium business up to 250 staff. i do work for not for profit and standard business.

Industry/Entity Type

Professional Service

Contact Information for Business Card

TALBrookWare Pty Ltd
A.C.N. 47 218 390 516
PO Box 827
Cleveland 4163
Mobile: 0400382957
Email: Dermot@Talbrookware.example.com.au

Font styles to use
Sans Serif

Colors

Designer to choose colors to be used in the design.

Requirements
Must have
• as a cloud based business it needs to have the this as the main theme. the tag line of Liftedpast the horizon should show we look at empowering business to get the most out of the cloud to minimise the spend they have as the target for the business is business and not for profits who need the make the most of their spend.
• the attached pictures are to be a source of insperation and key areas
Nice to have
• Quenfield Vorquel 820 is the core product that we sell and implentent for our clients so the theme should complement the Quenfield Vorquel theme

```html
<!DOCTYPE html>
<html lang="en">
<head>
<meta charset="utf-8">
<title>TALBrookWare Business Card</title>
<link href="https://fonts.googleapis.com/css2?family=Roboto:wght@400;700;900&display=swap" rel="stylesheet">
<style>
  :root {
    --backdrop: #8d8f8e;
    --card-light: #e6e7e9;
    --card-dark: #626365;
    --brand-blue: #0d8fd8;
    --ink-grey: #58595b;
    --band-grey: #5f6062;
    --divider-grey: #b8b9bb;
    --white: #ffffff;
  }
  * { margin: 0; padding: 0; box-sizing: border-box; }
  html, body { width: 1200px; height: 954px; overflow: hidden; }
  body {
    background: var(--backdrop);
    font-family: "Roboto", Arial, sans-serif;
    position: relative;
  }
  .card {
    position: absolute;
    left: 328px;
    width: 552px;
    height: 306px;
    box-shadow: 0 14px 18px rgba(0,0,0,0.25);
    overflow: hidden;
  }
  .card-front { top: 126px; background: var(--card-light); }
  .card-back  { top: 498px; background: var(--card-dark); }

  .brand {
    position: absolute;
    text-align: center;
    white-space: nowrap;
  }
  .card-front .brand { left: 30px; width: 236px; top: 156px; }
  .card-back .brand  { left: 0; width: 552px; top: 178px; }

  .brand-mark {
    display: inline-block;
    width: 14px; height: 14px;
    border-radius: 50%;
    background: var(--brand-blue);
    vertical-align: middle;
    margin-right: 7px;
  }
  .card-back .brand-mark { width: 20px; height: 20px; margin-right: 10px; }
  .brand-name {
    font-weight: 900;
    font-size: 27px;
    letter-spacing: -0.5px;
    color: var(--ink-grey);
    vertical-align: middle;
  }
  .card-back .brand-name { font-size: 36px; color: var(--white); }
  .brand-tagline {
    margin-top: 4px;
    font-size: 13px;
    color: var(--ink-grey);
  }
  .card-back .brand-tagline { font-size: 16px; color: var(--white); margin-top: 6px; }

  .divider {
    position: absolute;
    left: 272px; top: 78px;
    width: 1px; height: 144px;
    background: var(--divider-grey);
  }
  .contact {
    position: absolute;
    left: 298px; top: 76px;
    width: 236px;
    color: var(--ink-grey);
    font-size: 12.5px;
    line-height: 17px;
  }
  .contact-name {
    color: var(--brand-blue);
    font-weight: 700;
    font-size: 18px;
    margin-bottom: 12px;
  }
  .contact-address { margin-bottom: 9px; }
  .contact-row {
    display: flex;
    align-items: center;
    gap: 8px;
    font-size: 11.5px;
    white-space: nowrap;
  }
  .contact-row svg { width: 12px; height: 12px; flex: none; }
  .contact-acn { margin-top: 7px; }
  .edge-band { position: absolute; left: 0; bottom: 0; }
</style>
</head>
<body>

<section class="card card-front">
  <div class="brand">
    <span class="brand-mark"></span><span class="brand-name">TALBrookWare</span>
    <p class="brand-tagline">Lifted past the horizon</p>
  </div>

  <div class="divider"></div>

  <div class="contact">
    <h1 class="contact-name">DERMOT KESSLING</h1>
    <p class="contact-address">PO Box 827<br>Cleveland 4163</p>
    <p class="contact-row">
      <svg viewBox="0 0 16 16"><path d="M4 1.5l2.5 3-1.5 1.8c.8 1.8 2.2 3.2 4 4l1.8-1.5 3 2.5-1.6 2.4C7 13.5 2.5 9 1.7 3z" fill="var(--brand-blue)"/></svg>
      0400382957
    </p>
    <p class="contact-row">
      <svg viewBox="0 0 16 16"><rect x="1" y="3" width="14" height="10" fill="var(--brand-blue)"/><path d="M1.5 3.5L8 9l6.5-5.5" stroke="#fff" stroke-width="1.3" fill="none"/></svg>
      Dermot@Talbrookware.example.com.au
    </p>
    <p class="contact-row">
      <svg viewBox="0 0 16 16" fill="none" stroke="var(--brand-blue)" stroke-width="1.2"><circle cx="8" cy="8" r="6.5"/><ellipse cx="8" cy="8" rx="3" ry="6.5"/><path d="M1.5 8h13M2.5 4.8h11M2.5 11.2h11"/></svg>
      www.Talbrookware.example.com.au
    </p>
    <p class="contact-acn">A.C.N. 47 218 390 516</p>
  </div>

  <svg class="edge-band" width="552" height="14" viewBox="0 0 552 14">
    <polygon points="0,6 272,6 266,14 0,14" fill="var(--band-grey)"/>
    <polygon points="282,0 552,0 552,14 271,14" fill="var(--brand-blue)"/>
  </svg>
</section>

<section class="card card-back">
  <div class="brand">
    <span class="brand-mark"></span><span class="brand-name">TALBrookWare</span>
    <p class="brand-tagline">Lifted past the horizon</p>
  </div>
</section>

</body>
</html>
```